Brightwren Farming

We need a logo design for a new company based in Kelowna, BC. We grow market garden vegetables for sale at market and in a CSA program. We try to only use hand tools for all aspects of cultivating, seeding, weeding, harvesting and distributing. For this reason we consider ourselves very low impact on the environment.

We would like blues and green in the design with an earthy, natural feel

Target Market(s)

Environmentally aware, health conscience

Industry/Entity Type

Farming

Requirements
Must have
• Foot prints with section for contact details all on the one side
Should not have
• Dark, black colours or anything that looks unnatural

```html
<!DOCTYPE html>
<html lang="en">
<head>
<meta charset="utf-8">
<title>Brightwren Farming — Business Card</title>
<link href="https://fonts.googleapis.com/css2?family=Open+Sans:wght@400;600;700&display=swap" rel="stylesheet">
<style>
  :root {
    --backdrop: #1e1e1e;
    --card-white: #ffffff;
    --leaf-green: #4cb01c;
    --lime: #8dc100;
    --lime-light: #9acb1f;
    --ocean-blue: #0a5aa6;
    --name-blue: #1a6fc4;
    --ink: #333333;
  }
  * { margin: 0; padding: 0; box-sizing: border-box; }
  html, body {
    width: 1200px; height: 900px; overflow: hidden;
    background: var(--backdrop);
    font-family: "Open Sans", Arial, sans-serif;
  }
  .stage { position: relative; width: 1200px; height: 900px; }
  .card {
    position: absolute; top: 306px; width: 439px; height: 271px;
    border-radius: 10px; overflow: hidden;
    box-shadow: 0 2px 6px rgba(0,0,0,0.35);
  }
  .card--front { left: 149px; background: var(--card-white); }
  .card--back { left: 609px; background: var(--lime); }

  .name-tab { position: absolute; left: 0; top: 34px; }
  .person { position: absolute; left: 34px; top: 31px; }
  .person__name { font-size: 17px; font-weight: 700; line-height: 20px; }
  .person__first { color: var(--leaf-green); }
  .person__last { color: var(--name-blue); }
  .person__role { font-size: 11.5px; color: var(--ink); line-height: 16px; }

  .brand {
    position: absolute; display: flex; align-items: center; gap: 10px;
  }
  .brand__dot { width: 14px; height: 14px; border-radius: 50%; flex: none; }
  .brand__name { font-weight: 400; line-height: 1.05; text-align: left; }
  .card--front .brand { right: 26px; top: 92px; }
  .card--front .brand__dot { background: var(--leaf-green); }
  .card--front .brand__name { color: var(--leaf-green); font-size: 30px; }
  .card--back .brand { left: 112px; top: 110px; }
  .card--back .brand__dot { background: #ffffff; }
  .card--back .brand__name { color: #ffffff; font-size: 32px; }

  .contacts { position: absolute; left: 28px; top: 184px; list-style: none; }
  .contacts li {
    display: flex; align-items: center; gap: 5px;
    font-size: 12px; color: var(--ink); line-height: 16px;
  }
  .contacts svg { width: 9px; height: 9px; flex: none; }
  .address {
    position: absolute; right: 28px; top: 192px; text-align: right;
    font-size: 12px; color: var(--ink); line-height: 16px; font-style: normal;
  }
  .base-bands { position: absolute; left: 0; bottom: 0; }

  .tagline {
    position: absolute; left: 100px; top: 208px; width: 240px;
    text-align: center; color: #ffffff; font-size: 14.5px; line-height: 18px;
  }
</style>
</head>
<body>
<main class="stage">
  <section class="card card--front" aria-label="Business card front">
    <svg class="name-tab" width="26" height="32" viewBox="0 0 26 32">
      <polygon points="0,0 8,0 13,32 0,32" fill="var(--leaf-green)"/>
      <polygon points="9,0 25,0 25,32 14,32" fill="var(--ocean-blue)"/>
    </svg>
    <div class="person">
      <p class="person__name"><span class="person__first">Marcus</span> <span class="person__last">Hale</span></p>
      <p class="person__role">Managing Director</p>
    </div>

    <div class="brand">
      <span class="brand__dot"></span>
      <p class="brand__name">Brightwren<br>Farming</p>
    </div>

    <ul class="contacts">
      <li><svg viewBox="0 0 10 10"><path d="M2 1 L4 1 L4.6 3 L3.5 4 Q4.5 6 6 6.5 L7 5.4 L9 6 L9 8 Q6 9.5 3 6.5 Q0.5 4 2 1Z" fill="var(--leaf-green)"/></svg>123-456-7890</li>
      <li><svg viewBox="0 0 10 10"><rect x="0.5" y="2" width="9" height="6" fill="var(--leaf-green)"/><path d="M0.5 2 L5 5.5 L9.5 2" stroke="#fff" stroke-width="1" fill="none"/></svg>info@youremail.com</li>
      <li><svg viewBox="0 0 10 10"><path d="M4 6 L6 4 M3 5 L1.5 6.5 a1.5 1.5 0 0 0 2 2 L5 7 M7 5 L8.5 3.5 a1.5 1.5 0 0 0 -2 -2 L5 3" stroke="var(--leaf-green)" stroke-width="1.3" fill="none"/></svg>www.yourweb.com</li>
    </ul>
    <address class="address">1234, Address Goes Here<br>Country Name, 123456</address>

    <svg class="base-bands" width="439" height="20" viewBox="0 0 439 20">
      <polygon points="0,6 214,6 206,20 0,20" fill="var(--leaf-green)"/>
      <polygon points="222,1 439,1 439,20 207,20" fill="var(--ocean-blue)"/>
    </svg>
  </section>

  <section class="card card--back" aria-label="Business card back">
    <div class="brand">
      <span class="brand__dot"></span>
      <p class="brand__name">Brightwren<br>Farming</p>
    </div>
    <p class="tagline">cultivating, seeding, weeding, harvesting and distributing</p>
  </section>
</main>
</body>
</html>
```